Label for Dog Nourishing CBD Balm

Dear Designers,

We are looking for a packaging expert to design our new Hydrating Balm for dogs which contain a relaxing hemp extract (CBD). The product is intended to be massaged on the dog’s paws to make them softer and promote the animal’s well-being :)

Our company is already selling various relaxing cat & dog products, and we would like this new design to reflect the same "style & feeling" as our current products (see attached ZIP file).

Technical aspects:
- The packaging is a 40ml aluminium jar (58mm x 23mm).
- We are looking to design 2 separate labels (one for the front, one for the back)
- The label dimensions should be : 50mm x 50mm
- Please follow technical guidelines from printer (see ZIP file).

Design aspects:
- The design should be compatible with our brand identity (i.e. fluffly, pure, relaxing, positive, clean & natural).
- People should understand what the product "is" and what the product "does" simply from looking at the design.
- The actual balm is white/yellow in color.
- Soft/rounded shapes are preferred.
- Please use our brand's colors (see typo & colors in ZIP file)
- Please use our brand's fonts (see typo & colors in ZIP file)
- Please use our company logo (see ZIP file).
- The design also needs to convey a strong sense of professionalism as we are an animal "healthcare" brand.
- If you want to include a dog picture, we would prefer you to use a picture of our official brand ambassador (see ZIP file).
- Only original work (no plagiarism will be accepted).

Please don't hesitate to send us a message if you have any questions about the brand, the product or the design requirements.

We look forward to seeing your designs & working on this together !

Thanks & regards,
Marcus

Target Market(s)

Dog owners

Font styles to use
Other font styles liked:
• See ZIP file

Requirements
Must have
• Brand fonts (see typo & colors in ZIP file)
Brand colors (see typo & colors in ZIP file)

```html
<!DOCTYPE html>
<html lang="en">
<head>
<meta charset="utf-8">
<title>Soothing Balm – Jar Labels</title>
<link href="https://fonts.googleapis.com/css2?family=Archivo+Narrow:wght@400;700&family=Raleway:wght@300;400;600;700&display=swap" rel="stylesheet">
<style>
  :root{
    --page:#d9d9d9;
    --ink:#111111;
    --teal:#389b80;
    --teal-soft:#7fc4b1;
    --charcoal:#333333;
    --label-bg:#ececec;
    --back-bg:#ffffff;
  }
  *{margin:0;padding:0;box-sizing:border-box}
  html,body{width:936px;height:1200px;overflow:hidden;background:var(--page)}
  body{position:relative;font-family:"Raleway",sans-serif;color:var(--charcoal)}

  .sheet-title{position:absolute;left:79px;top:62px;font-family:"Archivo Narrow",sans-serif;font-weight:400;font-size:44px;color:var(--ink);letter-spacing:.5px}
  .sheet-title b{font-weight:700}
  .side-title{position:absolute;top:168px;font-family:"Archivo Narrow",sans-serif;font-weight:700;font-size:42px;color:var(--ink);letter-spacing:1.5px;text-align:center;width:326px}
  .side-title.front{left:123px}
  .side-title.back{left:489px}

  .label{position:absolute;top:255px;width:326px;height:326px;border-radius:50%;background:var(--teal)}
  .label.front{left:123px}
  .label.back{left:489px}
  .label-face{position:absolute;inset:17px;border-radius:50%;overflow:hidden;background:var(--label-bg)}
  .label.back .label-face{background:radial-gradient(circle at 40% 40%,#ffffff 0%,#f3f7f6 60%,#e8f1ee 100%)}
  .abs{position:absolute}

  .brand{left:0;width:100%;text-align:center;font-weight:600;color:var(--charcoal);letter-spacing:1px}
  .brand .dot{display:inline-block;width:8px;height:8px;border-radius:50%;background:var(--teal);margin-right:5px;vertical-align:middle;position:relative;top:-2px}

  .product-name{left:0;width:100%;text-align:center;font-size:26px;letter-spacing:.5px;line-height:1}
  .product-name .light,.back-name .light{font-weight:300;color:var(--teal)}
  .product-name .bold,.back-name .bold{font-weight:700;color:var(--charcoal)}

  .dog-photo{left:80px;top:102px;width:212px;height:200px;background:radial-gradient(ellipse at 45% 35%,#8f8a8e 0%,#b9b5b8 30%,#e6e6e6 60%,#f4f4f4 100%)}

  .cbd{left:3px;top:136px;width:78px;text-align:center;font-size:12px;line-height:1.3}
  .cbd b{font-weight:700;color:var(--charcoal)}
  .cbd span{font-weight:300;color:var(--teal)}

  .benefits{left:202px;top:112px;list-style:none;font-size:13px;line-height:18px;font-weight:300}
  .benefits li{display:flex;align-items:center}
  .benefits li::before{content:"";width:6px;height:6px;border-radius:50%;background:var(--charcoal);margin-right:3px}
  .benefits .teal{color:var(--teal)}
  .benefits .dark{color:var(--charcoal)}
  .benefits .dark::before{background:var(--teal)}

  .sub-name{left:0;width:100%;text-align:center;top:236px;font-size:21px;font-weight:300;color:var(--teal)}
  .weight{left:0;width:100%;text-align:center;top:260px;font-size:22px;font-weight:700;color:var(--charcoal)}

  .back-name{left:92px;top:4px;width:130px;text-align:right;font-size:19px;line-height:20px}
  .back-name .light{display:block;text-align:left}
  .section-head{left:0;width:100%;text-align:center;font-size:8.5px;font-weight:700;color:var(--charcoal)}
  .body-copy{left:35px;width:222px;text-align:center;font-size:8.3px;line-height:11.5px;font-weight:400;color:#444}
  .use-band{left:0;top:132px;width:292px;height:44px;background:var(--teal);border-radius:22px}
  .use-band .section-head{top:3px;color:#fff}
  .use-band p{position:absolute;left:14px;width:264px;top:13px;text-align:center;font-size:8px;line-height:8.5px;color:#fff}
  .distributor{left:72px;top:226px;width:92px;text-align:center;font-size:8.3px;line-height:9.5px;color:#444}
  .distributor b{font-weight:700;color:var(--charcoal)}
  .back-brand{left:166px;top:248px;font-size:12px;font-weight:600;letter-spacing:.5px;color:var(--charcoal)}
  .back-brand .dot{display:inline-block;width:6px;height:6px;border-radius:50%;background:var(--teal);margin-right:4px;vertical-align:middle;position:relative;top:-1px}
</style>
</head>
<body>
  <h1 class="sheet-title"><b>Label</b> for Nutritious CBD Balm for Dogs</h1>
  <h2 class="side-title front">GO AHEAD</h2>
  <h2 class="side-title back">BEHIND</h2>

  <section class="label front">
    <div class="label-face">
      <div class="abs dog-photo" role="img" aria-label="Photo of a wrinkled shar-pei dog resting its paws on a white towel"></div>
      <div class="abs brand" style="top:38px;font-size:18px"><span class="dot"></span>VERDANY</div>
      <div class="abs product-name" style="top:70px"><span class="light">SOOTHING</span> <span class="bold">BALM</span></div>
      <div class="abs cbd"><b>CBD</b> <span>250mg</span><br><span>0%</span> <b>THC</b></div>
      <ul class="abs benefits">
        <li class="teal">REPAIR</li>
        <li class="dark">NOURISH</li>
        <li class="teal">PROTECT</li>
      </ul>
      <div class="abs sub-name">Velo Balm™</div>
      <div class="abs weight">40g</div>
    </div>
  </section>

  <section class="label back">
    <div class="label-face">
      <div class="abs back-name"><span class="light">SOOTHING</span><span class="bold">BALM</span></div>
      <div class="abs section-head" style="top:52px">EVERYDAY RELAXATION</div>
      <p class="abs body-copy" style="top:63px">This balm repairs, nourishes and protects your dog's sensitive skin. Its trusted multi-action formula brings relief to fragile areas and soothes temporary irritations (paw pads, elbows, etc.)</p>
      <div class="abs use-band">
        <div class="abs section-head">RECOMMENDED USE:</div>
        <p>Rub a small amount of balm in the palm of your hand and apply to sensitive areas as a daily care ritual. Repeat until the product has been completely absorbed.</p>
      </div>
      <div class="abs section-head" style="top:183px">INGREDIENTS:</div>
      <p class="abs body-copy" style="top:194px;left:0;width:292px">Shea Butter, Beeswax, Coconut Oil, Hemp Extract (0% THC).</p>
      <p class="abs distributor">Distributed by:<br><b>VERDA EUROPE KFT.</b><br>Kert utca 12<br>1075 Budapest<br>Hungary</p>
      <div class="abs back-brand"><span class="dot"></span>VERDANY</div>
    </div>
  </section>
</body>
</html>
```